explains reason for march on Washington, DC

Important...I would like this to be an "oversized" card, but when I picked that choice, then having you design the card was not available. I hope this can still work.

This is not a business card. I will hand it to people who ask me about my idea to organize a march in Washington. On one side of the card will be a picture of Halvern Cemetery with the following words superimposed on the photo-(I want the graves to take center stage, with the words secondary)-the words are: "These men and women can, no longer, preserve our freedom." "That job now belongs to we, the living."

On the other side is this text:

If I am giving you this card, you have heard about my idea. I am following through on my idea to occupy the Senate and House Chambers on Memorial Day because I love America and the freedom that it has showered on me, a freedom that I see as being in great peril.

So, I am taking a stand.

You are free, of course, to think what you want about what I am doing. I am not looking for an argument, just a resolution about the future of the greatest nation on earth. To commit to joining this effort, go to forwendmere.example.

Thank you.
Tom Harker

You can be creative with the layout for these words.

Thank you.

Reason: I have been asked for a photo that is taking additional time. Thank you.

Hi.  The current deadline is for Feb. 27th, but I need to change it to this Saturday, Feb. 22nd.  My timeline has changed.  Please make submissions by 5 p.m. on Saturday.  That is my cut-off time and date.  Thank you.  Tom

```html
<!DOCTYPE html>
<html lang="en">
<head>
<meta charset="utf-8">
<title>The Living – Memorial Day Card</title>
<link href="https://fonts.googleapis.com/css2?family=Libre+Bodoni:wght@400;500;600;700&display=swap" rel="stylesheet">
<style>
  :root {
    --page: #ffffff;
    --banner: rgba(90, 90, 90, 0.96);
    --back: #333333;
    --ink-light: #ffffff;
    --sky: #d9dcd8;
    --trees: #5b6449;
    --grass: #5f9a3a;
    --stones: #e9e9e4;
  }
  * { margin: 0; padding: 0; box-sizing: border-box; }
  html, body {
    width: 1200px;
    height: 930px;
    overflow: hidden;
    background: var(--page);
  }
  .canvas {
    position: relative;
    width: 1200px;
    height: 930px;
    font-family: "Libre Bodoni", "Bodoni Moda", serif;
    color: var(--ink-light);
  }

  /* Front of card */
  .card-front {
    position: absolute;
    left: 62px;
    top: 73px;
    width: 617px;
    height: 477px;
    overflow: hidden;
  }
  .cemetery-photo {
    position: absolute;
    inset: 0;
    background: linear-gradient(180deg,
      var(--sky) 0%,
      #a9ad9c 18%,
      var(--trees) 45%,
      #6b7a55 62%,
      var(--grass) 78%,
      var(--stones) 100%);
  }
  .quote-banner {
    position: absolute;
    left: 79px;
    top: 81px;
    width: 538px;
    height: 139px;
    background: var(--banner);
  }
  .quote-mark {
    position: absolute;
    font-weight: 700;
    font-size: 118px;
    line-height: 1;
  }
  .quote-mark.open { left: 12px; top: 4px; }
  .quote-mark.close { left: 434px; top: 62px; }
  .quote-lead {
    position: absolute;
    left: 87px;
    top: 22px;
    font-size: 15.5px;
    font-weight: 500;
    line-height: 21px;
  }
  .quote-emphasis {
    position: absolute;
    left: 86px;
    top: 72px;
    font-size: 44px;
    font-weight: 400;
    letter-spacing: 3.5px;
    line-height: 1;
  }

  /* Back of card */
  .card-back {
    position: absolute;
    left: 500px;
    top: 377px;
    width: 619px;
    height: 481px;
    background: var(--back);
    padding: 64px 40px 0 45px;
    font-size: 13.6px;
    font-weight: 600;
    line-height: 18.2px;
  }
  .card-back p { margin-bottom: 18px; }
  .call-to-action {
    text-align: center;
    margin-bottom: 4px !important;
    padding-right: 20px;
  }
  .site-address {
    display: block;
    text-align: center;
    font-size: 27px;
    font-weight: 700;
    line-height: 34px;
    text-decoration: underline;
    text-decoration-thickness: 2px;
    text-underline-offset: 4px;
    margin: 0 0 20px -4px;
    padding-right: 20px;
    color: var(--ink-light);
  }
  .sign-off { margin-bottom: 0 !important; }
</style>
</head>
<body>
<div class="canvas">
  <section class="card-front">
    <div class="cemetery-photo" role="img" aria-label="Photo of Halvern Cemetery: an honor guard and horse-drawn caisson carrying a flag-draped casket past rows of white headstones under bare trees"></div>
    <div class="quote-banner">
      <span class="quote-mark open">“</span>
      <p class="quote-lead">Our fallen heroes can no longer preserve our freedom.<br>That job now belongs to us,</p>
      <p class="quote-emphasis">THE LIVING.</p>
      <span class="quote-mark close">”</span>
    </div>
  </section>

  <section class="card-back">
    <p>If I am giving you this card, you have heard about my idea. I am following<br>through on my idea to occupy the Senate and House Chambers on Memorial Day<br>because I love America and the freedom that it has showered on me, a freedom<br>that I see as being in great peril.</p>
    <p>So, I am taking a stand.</p>
    <p>You are free, of course, to think what you want about what I am doing. I am not<br>looking for an argument, just a resolution about the future of the greatest nation<br>on earth.</p>
    <p class="call-to-action">If you support my idea, then commit yourself to this effort at</p>
    <span class="site-address">www.forwendmere.example</span>
    <p class="sign-off">Thank you.<br>Tom Harker</p>
  </section>
</div>
</body>
</html>
```